PowerPoint Template Design for business consulting company in Silicon Valley

I need a PowerPoint template to use as the starting point for new presentations. I have a logo but now need design that supports this. I've attached a very descriptive PDF that explains exactly what I need. Here is a list of deliverables: 1. PowerPoint Template that I will use as the starter presentation for all new Vantor Bellway presentationsDesigns for the following slides: See picture below for examples of structure:2. Title slide with subtitle3. Section header4. Title and body5. Title and 2 columns6. Title and 3 columns7. One column text8. Editable timeline to show months, or steps for a process9. Bullet design for unordered list (can be graphic)10. Bullet design for ordered list11. Recommended fonts for each design: Title, subtitle, list, captionOPTIONAL: Possible graphic elements to be used for section title slide backgrounds or graphic elements:--Your team / my team / people on project--Goals for project / presentation--Editable Timeline--Speaking--Writing--Listening--People collaborating / helping each otherI am happy to accept proposals for developing these optional elements in a separate project.

Requirements
Must have
• Must be FLAT design.
• Not flashy or garish. Must be subtle.

```html
<!DOCTYPE html>
<html lang="en">
<head>
<meta charset="utf-8">
<title>Vantor Bellway – Presentation Template</title>
<link href="https://fonts.googleapis.com/css2?family=Open+Sans:wght@400;600;700&display=swap" rel="stylesheet">
<style>
:root{
  --bg:#c8c9ca;
  --green:#1f6a34;
  --green-soft:#2f8a46;
  --navy:#2b3a91;
  --navy-dark:#1f2a6e;
  --ink:#333;
  --muted:#8a8a8a;
  --line:#dcdcdc;
  --grey:#6f6f6f;
  --pale:#eeeeee;
}
*{box-sizing:border-box;margin:0;padding:0}
html,body{width:1200px;height:1108px;overflow:hidden;background:var(--bg)}
body{font-family:'Open Sans',sans-serif;position:relative}
.deck{position:absolute;left:56px;top:37px;display:grid;grid-template-columns:repeat(5,207px);grid-auto-rows:116px;gap:13px 12px}
.slide{position:relative;background:#fff;overflow:hidden;color:var(--ink)}
.hd{position:absolute;left:8px;top:6px;font-size:4.6px;font-weight:700;text-transform:uppercase;letter-spacing:.1px;color:#222}
.hd::before{content:"";position:absolute;left:-5px;top:-.5px;width:1.6px;height:6px;background:var(--navy)}
.ft{position:absolute;left:11px;right:6px;bottom:6px;border-top:.6px solid var(--line)}
.ft::before{content:"";position:absolute;left:-8px;top:-3px;width:5px;height:5px;border-radius:50%;border:.6px solid var(--green);background:#fff}
.ph{position:absolute}
.p{position:absolute;font-size:2.5px;line-height:3.3px;color:#777}
.p.w{color:#fff}
.box{position:absolute;color:#fff;font-size:2.5px;line-height:3.3px;padding:3px}
.g{background:var(--green)}
.n{background:var(--navy)}
.gr{background:var(--grey)}
.cap{position:absolute;font-size:3px;font-weight:700;text-align:center}
.dot{position:absolute;border-radius:50%}
.ico{position:absolute;width:7px;height:7px;border-radius:50%;background:var(--green)}
.ico.n{background:var(--navy)}
.lbl{position:absolute;font-size:2.4px;font-weight:700;text-align:center;color:#333}
svg{position:absolute;overflow:visible}
.photo-a{background:linear-gradient(135deg,#8b9aa8,#d9dde0 55%,#a7b2bb)}
.photo-b{background:linear-gradient(135deg,#cfd6de,#7f8ea0)}
.photo-c{background:linear-gradient(160deg,#c9b9a6,#efe8df 50%,#8d7f72)}
.photo-d{background:linear-gradient(135deg,#4d6a94,#b7c6dc)}
</style>
</head>
<body>
<main class="deck">

<!-- 1 title -->
<section class="slide" style="background:var(--navy)">
  <div class="ph" role="img" aria-label="Blue-toned photo of hands typing on a laptop" style="inset:0;background:linear-gradient(120deg,#3c4fa6,#27357f 60%,#1e2866)"></div>
  <div style="position:absolute;right:10px;top:12px;display:flex;align-items:center;gap:2px">
    <span style="width:5px;height:5px;border-radius:50%;background:#fff"></span>
    <span style="font-size:4.4px;font-weight:600;color:#fff">Vantor Bellway</span>
  </div>
  <div style="position:absolute;left:20px;top:70px;width:1px;height:18px;background:#fff"></div>
  <div style="position:absolute;left:24px;top:70px;color:#fff;font-size:8px;font-weight:600">Edit title here</div>
  <div style="position:absolute;left:24px;top:81px;color:#fff;font-size:4.6px">Edit subtitle here</div>
</section>

<!-- 2 two process columns -->
<section class="slide">
  <div class="hd">Edit title here</div>
  <div class="box g" style="left:38px;top:24px;width:54px;height:4px;padding:0"></div>
  <div class="box n" style="left:112px;top:24px;width:64px;height:4px;padding:0"></div>
  <div style="position:absolute;left:29px;top:36px;width:.8px;height:56px;background:var(--green)"></div>
  <div style="position:absolute;left:112px;top:36px;width:.8px;height:56px;background:var(--navy)"></div>
  <div class="dot g" style="left:26px;top:44px;width:7px;height:7px"></div>
  <div class="dot g" style="left:26px;top:62px;width:7px;height:7px"></div>
  <div class="dot g" style="left:26px;top:84px;width:7px;height:7px"></div>
  <div class="dot n" style="left:109px;top:44px;width:7px;height:7px"></div>
  <div class="dot n" style="left:109px;top:62px;width:7px;height:7px"></div>
  <div class="dot n" style="left:109px;top:84px;width:7px;height:7px"></div>
  <div class="box g" style="left:38px;top:40px;width:54px;height:14px">Lorem ipsum dolor sit amet, consectetur elit.</div>
  <div class="box g" style="left:38px;top:58px;width:54px;height:14px">Lorem ipsum dolor sit amet, consectetur elit.</div>
  <div class="box g" style="left:38px;top:80px;width:54px;height:14px">Lorem ipsum dolor sit amet, consectetur elit.</div>
  <div class="box n" style="left:122px;top:40px;width:54px;height:14px">Lorem ipsum dolor sit amet, consectetur elit.</div>
  <div class="box n" style="left:122px;top:58px;width:54px;height:14px">Lorem ipsum dolor sit amet, consectetur elit.</div>
  <div class="box n" style="left:122px;top:80px;width:54px;height:14px">Lorem ipsum dolor sit amet, consectetur elit.</div>
  <div class="ft"></div>
</section>

<!-- 3 about us -->
<section class="slide">
  <div class="hd">About us</div>
  <div class="box g" style="left:5px;top:26px;width:77px;height:76px;padding:4px">Lorem ipsum dolor sit amet, consectetur adipiscing elit. Sed do eiusmod tempor incididunt ut labore et dolore magna aliqua. Ut enim ad minim veniam, quis nostrud exercitation ullamco laboris nisi ut aliquip ex ea commodo consequat. Duis aute irure dolor in reprehenderit.</div>
  <div class="ph photo-c" role="img" aria-label="Team working together around a desk with laptops" style="left:82px;top:26px;width:125px;height:76px"></div>
  <div class="ft"></div>
</section>

<!-- 4 our team -->
<section class="slide">
  <div class="hd">Our team</div>
  <div class="dot photo-b" role="img" aria-label="Portrait of team member" style="left:22px;top:34px;width:24px;height:24px"></div>
  <div class="dot photo-b" role="img" aria-label="Portrait of team member" style="left:66px;top:34px;width:24px;height:24px"></div>
  <div class="dot photo-b" role="img" aria-label="Portrait of team member" style="left:110px;top:34px;width:24px;height:24px"></div>
  <div class="dot photo-b" role="img" aria-label="Portrait of team member" style="left:154px;top:34px;width:24px;height:24px"></div>
  <div class="lbl" style="left:14px;top:61px;width:40px;color:var(--navy)">MARA QUELL<br><span style="font-weight:400;color:#888">General Manager</span></div>
  <div class="lbl" style="left:58px;top:61px;width:40px;color:var(--navy)">IVO RENNER<br><span style="font-weight:400;color:#888">Travel Head</span></div>
  <div class="lbl" style="left:102px;top:61px;width:40px;color:var(--navy)">TEO ALVAR<br><span style="font-weight:400;color:#888">Finance</span></div>
  <div class="lbl" style="left:146px;top:61px;width:40px;color:var(--navy)">SOL BRANDT<br><span style="font-weight:400;color:#888">Senior Partner</span></div>
  <div class="p" style="left:12px;top:74px;width:183px">Lorem ipsum dolor sit amet, consectetur adipiscing elit, sed do eiusmod tempor incididunt ut labore et dolore magna aliqua. Ut enim ad minim veniam, quis nostrud exercitation ullamco laboris nisi ut aliquip ex ea commodo consequat duis aute.</div>
  <div class="ft"></div>
</section>

<!-- 5 numbered list -->
<section class="slide">
  <div class="hd">Edit title here</div>
  <div class="box g" style="left:26px;top:31px;width:9px;height:9px;font-size:3.5px;font-weight:700;padding:2.5px 1px">01</div>
  <div class="box g" style="left:26px;top:46px;width:9px;height:9px;font-size:3.5px;font-weight:700;padding:2.5px 1px">02</div>
  <div class="box g" style="left:26px;top:61px;width:9px;height:9px;font-size:3.5px;font-weight:700;padding:2.5px 1px">03</div>
  <div class="box g" style="left:26px;top:76px;width:9px;height:9px;font-size:3.5px;font-weight:700;padding:2.5px 1px">04</div>
  <div style="position:absolute;left:35px;top:31px;width:56px;height:9px;background:var(--pale);font-size:2.6px;padding:3px">Edit title here</div>
  <div style="position:absolute;left:35px;top:46px;width:56px;height:9px;background:var(--pale);font-size:2.6px;padding:3px">Edit title here</div>
  <div style="position:absolute;left:35px;top:61px;width:56px;height:9px;background:var(--pale);font-size:2.6px;padding:3px">Edit title here</div>
  <div style="position:absolute;left:35px;top:76px;width:56px;height:9px;background:var(--pale);font-size:2.6px;padding:3px">Edit title here</div>
  <div class="ph photo-a" role="img" aria-label="Business documents with charts and a laptop" style="left:99px;top:30px;width:80px;height:58px"></div>
  <div class="ft"></div>
</section>

<!-- 6 text + bar chart -->
<section class="slide">
  <div class="hd">Edit title here</div>
  <div class="p" style="left:8px;top:20px;width:94px">Lorem ipsum dolor sit amet, consectetur adipiscing elit, sed do eiusmod tempor incididunt ut labore et dolore magna aliqua. Ut enim ad minim veniam, quis nostrud exercitation ullamco laboris nisi ut aliquip ex ea commodo consequat. Duis aute irure dolor in reprehenderit in voluptate velit esse cillum dolore eu fugiat nulla pariatur. Excepteur sint occaecat cupidatat non proident, sunt in culpa qui officia deserunt mollit anim id est laborum. Sed ut perspiciatis unde omnis iste natus error sit voluptatem accusantium doloremque laudantium, totam rem aperiam eaque ipsa quae ab illo.</div>
  <svg viewBox="0 0 80 60" width="80" height="60" style="left:115px;top:34px">
    <line x1="6" y1="0" x2="6" y2="52" stroke="#ccc" stroke-width=".5"/>
    <line x1="6" y1="52" x2="78" y2="52" stroke="#ccc" stroke-width=".5"/>
    <rect x="12" y="42" width="5" height="10" fill="#2b3a91"/>
    <rect x="22" y="34" width="5" height="18" fill="#2b3a91"/>
    <rect x="32" y="26" width="5" height="26" fill="#2b3a91"/>
    <rect x="42" y="10" width="5" height="42" fill="#2b3a91"/>
    <rect x="52" y="22" width="5" height="30" fill="#2b3a91"/>
    <rect x="62" y="30" width="5" height="22" fill="#2b3a91"/>
    <rect x="35" y="1" width="14" height="5" fill="#1f6a34"/>
    <text x="42" y="4.6" font-size="2.6" fill="#fff" text-anchor="middle" font-family="Open Sans, sans-serif">Lorem</text>
  </svg>
  <div class="ft"></div>
</section>

<!-- 7 services -->
<section class="slide">
  <div class="hd">Our services</div>
  <div class="ph photo-a" role="img" aria-label="Laptop on an office desk" style="left:10px;top:20px;width:60px;height:50px"></div>
  <div class="ph photo-d" role="img" aria-label="Hand holding a tablet with charts" style="left:73px;top:20px;width:60px;height:50px"></div>
  <div class="ph photo-b" role="img" aria-label="People in a business meeting" style="left:136px;top:20px;width:60px;height:50px"></div>
  <div class="cap" style="left:10px;top:74px;width:60px;color:var(--navy)">Lorem ipsum dolor sit</div>
  <div class="cap" style="left:73px;top:74px;width:60px;color:var(--navy)">Lorem ipsum dolor sit</div>
  <div class="cap" style="left:136px;top:74px;width:60px;color:var(--navy)">Lorem ipsum dolor sit</div>
  <div class="p" style="left:12px;top:79px;width:56px;text-align:center">Lorem ipsum dolor sit amet, consectetur elit sed do eiusmod.</div>
  <div class="p" style="left:75px;top:79px;width:56px;text-align:center">Lorem ipsum dolor sit amet, consectetur elit sed do eiusmod.</div>
  <div class="p" style="left:138px;top:79px;width:56px;text-align:center">Lorem ipsum dolor sit amet, consectetur elit sed do eiusmod.</div>
  <div class="ft"></div>
</section>

<!-- 8 operations -->
<section class="slide">
  <div class="hd">Our operations</div>
  <div class="ico" style="left:36px;top:30px"></div><div class="ico" style="left:70px;top:30px"></div><div class="ico" style="left:104px;top:30px"></div><div class="ico" style="left:138px;top:30px"></div><div class="ico" style="left:172px;top:30px"></div>
  <div class="lbl" style="left:26px;top:40px;width:27px">LOREM IPSUM</div><div class="lbl" style="left:60px;top:40px;width:27px">LOREM IPSUM</div><div class="lbl" style="left:94px;top:40px;width:27px">LOREM IPSUM</div><div class="lbl" style="left:128px;top:40px;width:27px">LOREM IPSUM</div><div class="lbl" style="left:162px;top:40px;width:27px">LOREM IPSUM</div>
  <div class="ico" style="left:36px;top:66px"></div><div class="ico" style="left:70px;top:66px"></div><div class="ico" style="left:104px;top:66px"></div><div class="ico" style="left:138px;top:66px"></div><div class="ico" style="left:172px;top:66px"></div>
  <div class="lbl" style="left:26px;top:76px;width:27px">LOREM IPSUM</div><div class="lbl" style="left:60px;top:76px;width:27px">LOREM IPSUM</div><div class="lbl" style="left:94px;top:76px;width:27px">LOREM IPSUM</div><div class="lbl" style="left:128px;top:76px;width:27px">LOREM IPSUM</div><div class="lbl" style="left:162px;top:76px;width:27px">LOREM IPSUM</div>
  <div class="ft"></div>
</section>

<!-- 9 list + network photo -->
<section class="slide">
  <div class="hd">Edit title here</div>
  <div class="box g" style="left:10px;top:33px;width:5px;height:5px;font-size:2.6px;padding:.8px 1.5px">1</div>
  <div class="box g" style="left:10px;top:48px;width:5px;height:5px;font-size:2.6px;padding:.8px 1.5px">2</div>
  <div class="box g" style="left:10px;top:63px;width:5px;height:5px;font-size:2.6px;padding:.8px 1.5px">3</div>
  <div class="box g" style="left:10px;top:78px;width:5px;height:5px;font-size:2.6px;padding:.8px 1.5px">4</div>
  <div class="box g" style="left:10px;top:93px;width:5px;height:5px;font-size:2.6px;padding:.8px 1.5px">5</div>
  <div class="p" style="left:19px;top:34px">Lorem ipsum dolor sit amet, ut</div>
  <div class="p" style="left:19px;top:49px">Lorem ipsum dolor sit amet, ut</div>
  <div class="p" style="left:19px;top:64px">Lorem ipsum dolor sit amet, ut</div>
  <div class="p" style="left:19px;top:79px">Lorem ipsum dolor sit amet, ut</div>
  <div class="p" style="left:19px;top:94px">Lorem ipsum dolor sit amet, ut</div>
  <div class="ph" role="img" aria-label="Silhouettes of business people under a connected network" style="left:84px;top:0;width:123px;height:116px;background:linear-gradient(180deg,#d7dcef,#8d95c6 60%,#5b65a5)"></div>
  <div class="ft" style="right:130px"></div>
</section>

<!-- 10 world map -->
<section class="slide">
  <div class="hd">Edit title here</div>
  <div class="ph" role="img" aria-label="Grey world map with location pins" style="left:22px;top:14px;width:178px;height:74px;background:radial-gradient(ellipse at 50% 50%,#cfcfcf,#e9e9e9 70%,#fff)"></div>
  <div class="dot g" style="left:26px;top:80px;width:5px;height:5px"></div>
  <div class="lbl" style="left:34px;top:81px;text-align:left">EDIT TITLE HERE</div>
  <div class="dot n" style="left:26px;top:91px;width:5px;height:5px"></div>
  <div class="lbl" style="left:34px;top:92px;text-align:left">EDIT TITLE HERE</div>
  <div class="ft"></div>
</section>

<!-- 11 three colour boxes -->
<section class="slide">
  <div class="hd">Edit title here</div>
  <div class="box g" style="left:14px;top:24px;width:60px;height:76px;padding:34px 4px 0;text-align:center">Lorem ipsum dolor sit amet, consectetur adipiscing elit, sed do eiusmod tempor incididunt ut labore.</div>
  <div class="box gr" style="left:77px;top:24px;width:60px;height:76px;padding:34px 4px 0;text-align:center">Lorem ipsum dolor sit amet, consectetur adipiscing elit, sed do eiusmod tempor incididunt ut labore.</div>
  <div class="box n" style="left:140px;top:24px;width:60px;height:76px;padding:34px 4px 0;text-align:center">Lorem ipsum dolor sit amet, consectetur adipiscing elit, sed do eiusmod tempor incididunt ut labore.</div>
  <svg viewBox="0 0 14 12" width="14" height="12" style="left:37px;top:34px"><rect x="1" y="3" width="12" height="8" rx="1" fill="#fff"/><rect x="5" y="1" width="4" height="3" fill="none" stroke="#fff"/></svg>
  <svg viewBox="0 0 14 12" width="14" height="12" style="left:100px;top:34px"><circle cx="7" cy="4" r="3" fill="#fff"/><rect x="2" y="8" width="10" height="4" rx="2" fill="#fff"/></svg>
  <svg viewBox="0 0 14 12" width="14" height="12" style="left:163px;top:34px"><polygon points="7,1 14,5 7,9 0,5" fill="#fff"/><rect x="4" y="7" width="6" height="4" fill="#fff"/></svg>
  <div class="ft"></div>
</section>

<!-- 12 icons + photo -->
<section class="slide">
  <div class="hd">Edit title here</div>
  <div class="ico" style="left:24px;top:28px"></div><div class="ico" style="left:58px;top:28px"></div><div class="ico" style="left:92px;top:28px"></div>
  <div class="lbl" style="left:15px;top:37px;width:25px">LOREM IPSUM</div><div class="lbl" style="left:49px;top:37px;width:25px">LOREM IPSUM</div><div class="lbl" style="left:83px;top:37px;width:25px">LOREM IPSUM</div>
  <div class="ico" style="left:24px;top:66px"></div><div class="ico" style="left:58px;top:66px"></div><div class="ico" style="left:92px;top:66px"></div>
  <div class="lbl" style="left:15px;top:75px;width:25px">LOREM IPSUM</div><div class="lbl" style="left:49px;top:75px;width:25px">LOREM IPSUM</div><div class="lbl" style="left:83px;top:75px;width:25px">LOREM IPSUM</div>
  <div class="ph photo-c" role="img" aria-label="Group of colleagues talking in an office" style="left:135px;top:10px;width:64px;height:96px"></div>
  <div class="ft" style="right:75px"></div>
</section>

<!-- 13 section title navy -->
<section class="slide" style="background:var(--navy)">
  <div style="position:absolute;left:0;right:0;top:68px;border-top:.6px solid rgba(255,255,255,.6)"></div>
  <div style="position:absolute;left:0;right:0;top:100px;border-top:.6px solid rgba(255,255,255,.6)"></div>
  <div style="position:absolute;left:0;right:0;top:68px;height:32px;background:var(--navy-dark)"></div>
  <svg viewBox="0 0 14 12" width="14" height="12" style="left:22px;top:78px"><rect x="1" y="3" width="12" height="8" rx="1" fill="#fff"/><rect x="5" y="1" width="4" height="3" fill="none" stroke="#fff"/></svg>
  <div style="position:absolute;left:48px;top:74px;color:#fff;font-size:8px;font-weight:600">Section Title</div>
  <div class="p w" style="left:48px;top:86px;width:90px">Lorem ipsum dolor sit amet, consectetur adipiscing elit, sed do eiusmod tempor.</div>
</section>

<!-- 14 company overview two boxes -->
<section class="slide">
  <div class="hd">Company overview</div>
  <div class="box g" style="left:10px;top:28px;width:91px;height:60px;padding:5px">• Lorem ipsum dolor sit amet, consectetur adipiscing elit, sed do eiusmod tempor incididunt ut labore et dolore magna aliqua. Ut enim ad minim veniam, quis nostrud exercitation ullamco laboris nisi ut aliquip ex ea commodo.</div>
  <div class="box n" style="left:104px;top:28px;width:91px;height:60px;padding:5px">• Lorem ipsum dolor sit amet, consectetur adipiscing elit, sed do eiusmod tempor incididunt ut labore et dolore magna aliqua. Ut enim ad minim veniam, quis nostrud exercitation ullamco laboris nisi ut aliquip ex ea commodo.</div>
  <div style="position:absolute;left:10px;top:88px;width:185px;height:2px;background:#777"></div>
  <div class="ft"></div>
</section>

<!-- 15 photo band A B C D -->
<section class="slide">
  <div class="hd">Edit title here</div>
  <div class="p" style="left:8px;top:14px">Lorem ipsum dolor sit amet, consectetur adipiscing elit. Aenean sed tempor lorem.</div>
  <div class="ph photo-c" role="img" aria-label="Four smiling colleagues in front of a brick wall" style="left:8px;top:20px;width:190px;height:40px"></div>
  <div class="box g" style="left:8px;top:60px;width:44px;height:6px;padding:1.5px;text-align:center;font-size:3px">A</div>
  <div class="box n" style="left:56px;top:60px;width:44px;height:6px;padding:1.5px;text-align:center;font-size:3px">B</div>
  <div class="box g" style="left:104px;top:60px;width:44px;height:6px;padding:1.5px;text-align:center;font-size:3px">C</div>
  <div class="box n" style="left:152px;top:60px;width:46px;height:6px;padding:1.5px;text-align:center;font-size:3px">D</div>
  <div class="p" style="left:8px;top:70px;width:44px;text-align:center">Lorem ipsum dolor sit amet, consectetur elit.</div>
  <div class="p" style="left:56px;top:70px;width:44px;text-align:center">Lorem ipsum dolor sit amet, consectetur elit.</div>
  <div class="p" style="left:104px;top:70px;width:44px;text-align:center">Lorem ipsum dolor sit amet, consectetur elit.</div>
  <div class="p" style="left:152px;top:70px;width:46px;text-align:center">Lorem ipsum dolor sit amet, consectetur elit.</div>
  <div class="ft"></div>
</section>

<!-- 16 company overview icon columns -->
<section class="slide">
  <div class="hd">Company overview</div>
  <div class="p" style="left:30px;top:27px;width:58px;text-align:right">Lorem ipsum dolor<br>sit amet consectetur</div>
  <div class="p" style="left:30px;top:46px;width:58px;text-align:right">Lorem ipsum dolor<br>sit amet consectetur</div>
  <div class="p" style="left:30px;top:65px;width:58px;text-align:right">Lorem ipsum dolor<br>sit amet consectetur</div>
  <div class="p" style="left:30px;top:84px;width:58px;text-align:right">Lorem ipsum dolor<br>sit amet consectetur</div>
  <div class="ico n" style="left:92px;top:27px;width:9px;height:9px"></div><div class="ico n" style="left:92px;top:46px;width:9px;height:9px"></div><div class="ico n" style="left:92px;top:65px;width:9px;height:9px"></div><div class="ico n" style="left:92px;top:84px;width:9px;height:9px"></div>
  <div style="position:absolute;left:108px;top:24px;height:74px;border-left:.6px solid var(--line)"></div>
  <div class="ico" style="left:114px;top:27px;width:9px;height:9px"></div><div class="ico" style="left:114px;top:46px;width:9px;height:9px"></div><div class="ico" style="left:114px;top:65px;width:9px;height:9px"></div><div class="ico" style="left:114px;top:84px;width:9px;height:9px"></div>
  <div class="p" style="left:127px;top:27px;width:60px">Lorem ipsum dolor<br>sit amet consectetur</div>
  <div class="p" style="left:127px;top:46px;width:60px">Lorem ipsum dolor<br>sit amet consectetur</div>
  <div class="p" style="left:127px;top:65px;width:60px">Lorem ipsum dolor<br>sit amet consectetur</div>
  <div class="p" style="left:127px;top:84px;width:60px">Lorem ipsum dolor<br>sit amet consectetur</div>
  <div class="ft"></div>
</section>

<!-- 17 navy panel + photo -->
<section class="slide">
  <div class="hd">Edit title here</div>
  <div class="box n" style="left:0;top:18px;width:60px;height:84px;padding:6px;font-size:3px;line-height:4px;font-weight:600">Lorem ipsum dolor sit amet consectetur adipiscing elit. Cras bibendum mattis leo, ac efficitur ipsum lobortis non. Praesent vitae pulvinar lorem.</div>
  <div class="ph photo-b" role="img" aria-label="Business people walking through a bright office lobby" style="left:60px;top:18px;width:147px;height:84px"></div>
  <div style="position:absolute;left:58px;top:42px;width:120px;height:30px;background:#fff"></div>
  <div class="ico" style="left:74px;top:48px;border-radius:1px"></div><div class="ico" style="left:112px;top:48px;border-radius:1px"></div><div class="ico" style="left:150px;top:48px;border-radius:1px"></div>
  <div class="lbl" style="left:66px;top:60px;width:23px">LOREM</div><div class="lbl" style="left:104px;top:60px;width:23px">LOREM</div><div class="lbl" style="left:142px;top:60px;width:23px">LOREM</div>
  <div class="ft"></div>
</section>

<!-- 18 puzzle -->
<section class="slide">
  <div class="hd">Edit title here</div>
  <div class="ph" role="img" aria-label="Interlocking green and blue puzzle pieces" style="left:80px;top:28px;width:52px;height:56px;background:linear-gradient(135deg,var(--navy) 0 30%,var(--green) 30% 60%,var(--navy) 60%);clip-path:polygon(50% 0,100% 40%,70% 100%,0 70%)"></div>
  <div class="p" style="left:128px;top:26px;width:50px"><b style="color:#333">Lorem ipsum dolor sit</b><br>Lorem ipsum dolor sit amet.</div>
  <div class="p" style="left:140px;top:60px;width:50px"><b style="color:#333">Lorem ipsum dolor sit</b><br>Lorem ipsum dolor sit amet.</div>
  <div class="p" style="left:28px;top:52px;width:50px;text-align:right"><b style="color:#333">Lorem ipsum dolor sit</b><br>Lorem ipsum dolor sit amet.</div>
  <div class="p" style="left:60px;top:86px;width:50px;text-align:right"><b style="color:#333">Lorem ipsum dolor sit</b><br>Lorem ipsum dolor sit amet.</div>
  <div class="ft"></div>
</section>

<!-- 19 green band portraits -->
<section class="slide">
  <div class="hd">Edit title here</div>
  <div class="g" style="position:absolute;left:0;right:0;top:50px;height:52px"></div>
  <div class="dot photo-b" role="img" aria-label="Portrait of team member" style="left:42px;top:30px;width:24px;height:24px;border:1px solid #fff"></div>
  <div class="dot photo-b" role="img" aria-label="Portrait of team member" style="left:92px;top:30px;width:24px;height:24px;border:1px solid #fff"></div>
  <div class="dot photo-b" role="img" aria-label="Portrait of team member" style="left:142px;top:30px;width:24px;height:24px;border:1px solid #fff"></div>
  <div class="lbl" style="left:34px;top:58px;width:40px;color:#fff;font-size:3px">LOREM IPSUM</div>
  <div class="lbl" style="left:84px;top:58px;width:40px;color:#fff;font-size:3px">LOREM IPSUM</div>
  <div class="lbl" style="left:134px;top:58px;width:40px;color:#fff;font-size:3px">LOREM IPSUM</div>
  <div class="ft"></div>
</section>

<!-- 20 table -->
<section class="slide">
  <div class="hd">Edit title here</div>
  <svg viewBox="0 0 180 62" width="180" height="62" style="left:14px;top:30px" font-family="Open Sans, sans-serif" font-size="2.6" text-anchor="middle">
    <rect x="0" y="0" width="180" height="8" fill="#2b3a91"/>
    <rect x="0" y="8" width="180" height="9" fill="#eeeeee"/><rect x="0" y="17" width="180" height="9" fill="#dcdcdc"/>
    <rect x="0" y="26" width="180" height="9" fill="#eeeeee"/><rect x="0" y="35" width="180" height="9" fill="#dcdcdc"/>
    <rect x="0" y="44" width="180" height="9" fill="#eeeeee"/><rect x="0" y="53" width="180" height="9" fill="#dcdcdc"/>
    <g fill="#fff" font-weight="700"><text x="22" y="5">Lorem</text><text x="67" y="5">Lorem</text><text x="112" y="5">Lorem</text><text x="157" y="5">Lorem</text></g>
    <g fill="#555">
      <text x="22" y="13.5">Lorem</text><text x="67" y="13.5">Lorem</text><text x="112" y="13.5">Lorem</text><text x="157" y="13.5">Lorem</text>
      <text x="22" y="22.5">Lorem</text><text x="67" y="22.5">Lorem</text><text x="112" y="22.5">Lorem</text><text x="157" y="22.5">Lorem</text>
      <text x="22" y="31.5">Lorem</text><text x="67" y="31.5">Lorem</text><text x="112" y="31.5">Lorem</text><text x="157" y="31.5">Lorem</text>
      <text x="22" y="40.5">Lorem</text><text x="67" y="40.5">Lorem</text><text x="112" y="40.5">Lorem</text><text x="157" y="40.5">Lorem</text>
      <text x="22" y="49.5">Lorem</text><text x="67" y="49.5">Lorem</text><text x="112" y="49.5">Lorem</text><text x="157" y="49.5">Lorem</text>
      <text x="22" y="58.5">Lorem</text><text x="67" y="58.5">Lorem</text><text x="112" y="58.5">Lorem</text><text x="157" y="58.5">Lorem</text>
    </g>
  </svg>
  <div class="ft"></div>
</section>

<!-- 21 three tiles -->
<section class="slide">
  <div class="hd">Edit title here</div>
  <div class="ph photo-d" role="img" aria-label="Car on a blue background" style="left:10px;top:18px;width:55px;height:46px"></div>
  <div class="ph" role="img" aria-label="Wireless router on a teal background" style="left:76px;top:18px;width:55px;height:46px;background:linear-gradient(135deg,#8fd0d8,#2d8aa0)"></div>
  <div class="ph n" role="img" aria-label="House icon on a navy background" style="left:142px;top:18px;width:55px;height:46px"></div>
  <div class="cap" style="left:10px;top:68px;width:55px;color:var(--green)">LOREM IPSUM</div>
  <div class="cap" style="left:76px;top:68px;width:55px;color:var(--green)">LOREM IPSUM</div>
  <div class="cap" style="left:142px;top:68px;width:55px;color:var(--green)">LOREM IPSUM</div>
  <div class="p" style="left:12px;top:73px;width:51px;text-align:center">Lorem ipsum dolor sit amet, consectetur adipiscing elit. Curabitur nulla ligula.</div>
  <div class="p" style="left:78px;top:73px;width:51px;text-align:center">Lorem ipsum dolor sit amet, consectetur adipiscing elit. Curabitur nulla ligula.</div>
  <div class="p" style="left:144px;top:73px;width:51px;text-align:center">Lorem ipsum dolor sit amet, consectetur adipiscing elit. Curabitur nulla ligula.</div>
  <div class="ft"></div>
</section>

<!-- 22 green bar chart -->
<section class="slide">
  <div class="hd">Edit title here</div>
  <svg viewBox="0 0 80 70" width="80" height="70" style="left:14px;top:22px">
    <line x1="4" y1="0" x2="4" y2="62" stroke="#ccc" stroke-width=".5"/>
    <line x1="4" y1="62" x2="80" y2="62" stroke="#ccc" stroke-width=".5"/>
    <rect x="12" y="52" width="7" height="10" fill="#1f6a34"/>
    <rect x="24" y="46" width="7" height="16" fill="#1f6a34"/>
    <rect x="36" y="38" width="7" height="24" fill="#1f6a34"/>
    <rect x="48" y="30" width="7" height="32" fill="#1f6a34"/>
    <rect x="60" y="20" width="7" height="42" fill="#1f6a34"/>
    <polyline points="14,48 28,40 40,32 52,22 64,12 76,2" fill="none" stroke="#999" stroke-width=".5"/>
  </svg>
  <div class="dot g" style="left:16px;top:96px;width:4px;height:4px"></div><div class="dot g" style="left:32px;top:96px;width:4px;height:4px"></div><div class="dot g" style="left:48px;top:96px;width:4px;height:4px"></div><div class="dot g" style="left:64px;top:96px;width:4px;height:4px"></div><div class="dot g" style="left:80px;top:96px;width:4px;height:4px"></div>
  <div class="p" style="left:108px;top:18px;width:90px">Lorem ipsum dolor sit amet, consectetur adipiscing elit, sed do eiusmod tempor incididunt ut labore et dolore magna aliqua. Ut enim ad minim veniam, quis nostrud exercitation ullamco laboris nisi ut aliquip ex ea commodo consequat. Duis aute irure dolor in reprehenderit in voluptate velit esse cillum dolore eu fugiat nulla pariatur. Excepteur sint occaecat cupidatat non proident, sunt in culpa qui officia deserunt mollit anim id est laborum ipsum dolor.</div>
  <div class="ft"></div>
</section>

<!-- 23 photo + green box -->
<section class="slide">
  <div class="hd">Edit title here</div>
  <div class="ph photo-c" role="img" aria-label="Colleagues collaborating at a table" style="left:0;top:22px;width:207px;height:80px"></div>
  <div class="box g" style="left:22px;top:22px;width:64px;height:80px;padding:5px">
    <div style="font-size:4.4px;font-weight:700;margin-bottom:3px">LOREM IPSUM</div>
    Lorem ipsum dolor sit amet, consectetur adipiscing elit, sed do eiusmod tempor incididunt ut labore et dolore magna aliqua. Ut enim ad minim veniam, quis nostrud exercitation ullamco laboris.
  </div>
  <div class="ft"></div>
</section>

<!-- 24 text + navy boxes on photo -->
<section class="slide">
  <div class="hd">Edit title here</div>
  <div class="p" style="left:8px;top:20px;width:62px">Lorem ipsum dolor sit amet, consectetur adipiscing elit. Donec lorem nibh, vehicula at molestie vitae, pretium sit amet. Phasellus ut lacus vel felis vestibulum. Nunc eget turpis. Nullam vitae leo nec magna pulvinar volutpat. Integer quis sagittis lorem, quis hendrerit.</div>
  <div class="ph photo-d" role="img" aria-label="City office building background" style="left:70px;top:18px;width:137px;height:84px"></div>
  <div class="box n" style="left:78px;top:20px;width:56px;height:68px"><b style="font-size:3px">Lorem ipsum</b><br>Lorem ipsum dolor sit amet, consectetur adipiscing elit. Duis ut nunc vitae arcu mattis vel volutpat.</div>
  <div class="box n" style="left:138px;top:20px;width:56px;height:68px"><b style="font-size:3px">Lorem ipsum</b><br>Lorem ipsum dolor sit amet, consectetur adipiscing elit. Duis ut nunc vitae arcu mattis vel volutpat.</div>
  <div class="ft"></div>
</section>

<!-- 25 diamond grid + photo -->
<section class="slide">
  <div class="hd">Edit title here</div>
  <div style="position:absolute;left:12px;top:30px;width:38px;height:26px;border:.6px solid var(--green)"></div>
  <div style="position:absolute;left:54px;top:30px;width:38px;height:26px;border:.6px solid var(--green)"></div>
  <div style="position:absolute;left:96px;top:30px;width:38px;height:26px;border:.6px solid var(--green)"></div>
  <div style="position:absolute;left:12px;top:60px;width:38px;height:26px;border:.6px solid var(--green)"></div>
  <div style="position:absolute;left:54px;top:60px;width:38px;height:26px;border:.6px solid var(--green)"></div>
  <div style="position:absolute;left:96px;top:60px;width:38px;height:26px;border:.6px solid var(--green)"></div>
  <div class="g" style="position:absolute;left:27px;top:26px;width:8px;height:8px;transform:rotate(45deg)"></div>
  <div class="g" style="position:absolute;left:69px;top:26px;width:8px;height:8px;transform:rotate(45deg)"></div>
  <div class="g" style="position:absolute;left:111px;top:26px;width:8px;height:8px;transform:rotate(45deg)"></div>
  <div class="g" style="position:absolute;left:27px;top:80px;width:8px;height:8px;transform:rotate(45deg)"></div>
  <div class="g" style="position:absolute;left:69px;top:80px;width:8px;height:8px;transform:rotate(45deg)"></div>
  <div class="g" style="position:absolute;left:111px;top:80px;width:8px;height:8px;transform:rotate(45deg)"></div>
  <div class="p" style="left:14px;top:40px;width:34px;text-align:center">Lorem ipsum dolor sit amet</div>
  <div class="p" style="left:56px;top:40px;width:34px;text-align:center">Lorem ipsum dolor sit amet</div>
  <div class="p" style="left:98px;top:40px;width:34px;text-align:center">Lorem ipsum dolor sit amet</div>
  <div class="p" style="left:14px;top:66px;width:34px;text-align:center">Lorem ipsum dolor sit amet</div>
  <div class="p" style="left:56px;top:66px;width:34px;text-align:center">Lorem ipsum dolor sit amet</div>
  <div class="p" style="left:98px;top:66px;width:34px;text-align:center">Lorem ipsum dolor sit amet</div>
  <div class="ph" role="img" aria-label="Finger touching a glowing digital screen" style="left:150px;top:18px;width:57px;height:84px;background:linear-gradient(135deg,#d6eef1,#5aa9b8 60%,#2a6f85)"></div>
  <div class="ft" style="right:60px"></div>
</section>

<!-- 26 org chart -->
<section class="slide">
  <div class="hd">Edit title here</div>
  <svg viewBox="0 0 207 116" width="207" height="116" style="left:0;top:0" font-family="Open Sans, sans-serif" font-size="2.3" text-anchor="middle">
    <g stroke="#bbb" stroke-width=".5" fill="none">
      <path d="M103 30V36M34 36H172M34 36V40M172 36V40M103 36V40M80 44H126M80 44V70M126 44V70M80 52H72M126 52H134M80 62H72M126 62H134M80 70H72M126 70H134"/>
    </g>
    <rect x="87" y="24" width="32" height="6" fill="#1f6a34"/><text x="103" y="28" fill="#fff">Title Goes Here</text>
    <rect x="18" y="40" width="32" height="6" fill="#1f6a34"/><text x="34" y="44" fill="#fff">Title Goes Here</text>
    <rect x="156" y="40" width="32" height="6" fill="#1f6a34"/><text x="172" y="44" fill="#fff">Title Goes Here</text>
    <rect x="56" y="49" width="32" height="6" fill="#2b3a91"/><text x="72" y="53" fill="#fff">Title Goes Here</text>
    <rect x="118" y="49" width="32" height="6" fill="#2b3a91"/><text x="134" y="53" fill="#fff">Title Goes Here</text>
    <rect x="56" y="59" width="32" height="6" fill="#2b3a91"/><text x="72" y="63" fill="#fff">Title Goes Here</text>
    <rect x="118" y="59" width="32" height="6" fill="#2b3a91"/><text x="134" y="63" fill="#fff">Title Goes Here</text>
    <rect x="56" y="69" width="32" height="6" fill="#2b3a91"/><text x="72" y="73" fill="#fff">Title Goes Here</text>
    <rect x="118" y="69" width="32" height="6" fill="#2b3a91"/><text x="134" y="73" fill="#fff">Title Goes Here</text>
  </svg>
  <div class="p" style="left:12px;top:84px;width:183px;text-align:center">Lorem ipsum dolor sit amet, consectetur adipiscing elit, sed do eiusmod tempor incididunt ut labore et dolore magna aliqua. Ut enim ad minim veniam, quis nostrud exercitation ullamco laboris nisi ut aliquip ex ea commodo consequat.</div>
  <div class="ft"></div>
</section>

<!-- 27 tabs -->
<section class="slide">
  <div class="hd">Edit title here</div>
  <div style="position:absolute;left:0;right:0;top:22px;height:38px;background:var(--pale)"></div>
  <div class="dot" style="left:38px;top:26px;width:8px;height:8px;background:#fff;border:.6px solid var(--green)"></div>
  <div class="dot" style="left:86px;top:26px;width:8px;height:8px;background:#fff;border:.6px solid var(--navy)"></div>
  <div class="dot" style="left:134px;top:26px;width:8px;height:8px;background:#fff;border:.6px solid #777"></div>
  <div class="box g" style="left:30px;top:34px;width:46px;height:18px"><b style="font-size:3px">Lorem ipsum</b><br>Lorem ipsum dolor sit amet consectetur.</div>
  <div class="box n" style="left:78px;top:34px;width:46px;height:18px"><b style="font-size:3px">Lorem ipsum</b><br>Lorem ipsum dolor sit amet consectetur.</div>
  <div class="box gr" style="left:126px;top:34px;width:46px;height:18px"><b style="font-size:3px">Lorem ipsum</b><br>Lorem ipsum dolor sit amet consectetur.</div>
  <div class="p" style="left:14px;top:66px;width:180px">Lorem ipsum dolor sit amet, consectetur adipiscing elit, sed do eiusmod tempor incididunt ut labore et dolore magna aliqua. Ut enim ad minim veniam, quis nostrud exercitation ullamco laboris nisi ut aliquip ex ea commodo consequat. Duis aute irure dolor in reprehenderit in voluptate velit.</div>
  <div class="ft"></div>
</section>

<!-- 28 text + icon tree -->
<section class="slide">
  <div class="hd">Edit title here</div>
  <div class="p" style="left:8px;top:18px;width:88px">Lorem ipsum dolor sit amet, consectetur adipiscing elit, sed do eiusmod tempor incididunt ut labore et dolore magna aliqua. Ut enim ad minim veniam, quis nostrud exercitation ullamco laboris nisi ut aliquip ex ea commodo consequat. Duis aute irure dolor in reprehenderit in voluptate velit esse cillum dolore eu fugiat nulla pariatur. Excepteur sint occaecat cupidatat non proident, sunt in culpa qui officia deserunt mollit anim id est laborum. Sed ut perspiciatis unde omnis iste natus error sit voluptatem accusantium doloremque laudantium, totam rem aperiam.</div>
  <div class="ph" role="img" aria-label="Tree of green and blue circles containing business icons" style="left:112px;top:18px;width:80px;height:82px;border-radius:50% 50% 20% 20%;background:radial-gradient(circle at 50% 40%,#2f8a46,#1f6a34 45%,#2b3a91 70%,#fff 72%)"></div>
  <div class="ft"></div>
</section>

<!-- 29 quote navy -->
<section class="slide" style="background:var(--navy)">
  <div class="ph" role="img" aria-label="Navy-tinted city skyline" style="inset:0;background:linear-gradient(180deg,#3a4aa3,#26347f)"></div>
  <div style="position:absolute;left:16px;top:6px;color:#fff;font-size:22px;font-weight:700;line-height:1">“</div>
  <div style="position:absolute;left:20px;top:30px;width:168px;color:#fff;font-size:4.6px;line-height:5.8px;font-weight:600;text-align:center">Lorem ipsum dolor sit amet, consectetur adipiscing elit. Phasellus sodales, ligula ultrices tempus tristique, tellus justo aliquam dui, nec Lorem ipsum dolor sit amet, consectetur adipiscing elit. Phasellus sodales, ligula ultrices tempus tristique, tellus justo aliquam dui, nec Lorem ipsum dolor sit amet, consectetur adipiscing elit.</div>
  <div style="position:absolute;left:80px;top:92px;color:#fff;font-size:5px;font-weight:700">- REN HALVIK</div>
  <div style="position:absolute;right:14px;top:84px;color:#fff;font-size:22px;font-weight:700;line-height:1">”</div>
</section>

<!-- 30 building + pie -->
<section class="slide">
  <div class="hd">Edit title here</div>
  <div class="ph" role="img" aria-label="Modern glass office building under a blue sky" style="left:8px;top:18px;width:192px;height:32px;background:linear-gradient(180deg,#8fb3d8,#4e6f95 70%,#3b7a3f)"></div>
  <div class="p" style="left:8px;top:54px;width:100px">Lorem ipsum dolor sit amet, consectetur adipiscing elit, sed do eiusmod tempor incididunt ut labore et dolore magna aliqua. Ut enim ad minim veniam, quis nostrud exercitation ullamco laboris nisi ut aliquip ex ea commodo consequat. Duis aute irure dolor in reprehenderit.</div>
  <svg viewBox="0 0 40 40" width="40" height="40" style="left:118px;top:56px">
    <circle cx="20" cy="20" r="18" fill="#1f6a34"/>
    <path d="M20 20L20 2A18 18 0 0 1 37 14Z" fill="#2f8a46"/>
    <path d="M20 20L37 14A18 18 0 0 1 30 35Z" fill="#174f27"/>
    <text x="12" y="14" font-size="3" fill="#fff" font-family="Open Sans, sans-serif">15%</text>
    <text x="25" y="24" font-size="3" fill="#fff" font-family="Open Sans, sans-serif">40%</text>
    <text x="8" y="26" font-size="3" fill="#fff" font-family="Open Sans, sans-serif">25%</text>
  </svg>
  <div class="p" style="left:168px;top:58px">— Edit title here</div>
  <div class="p" style="left:168px;top:68px">— Edit title here</div>
  <div class="p" style="left:168px;top:78px">— Edit title here</div>
  <div class="p" style="left:168px;top:88px">— Edit title here</div>
  <div class="ft"></div>
</section>

<!-- 31 two photos -->
<section class="slide">
  <div class="hd">Edit title here</div>
  <div class="ph photo-d" role="img" aria-label="Hands typing on a laptop with glowing data" style="left:22px;top:20px;width:74px;height:44px"></div>
  <div class="ph photo-a" role="img" aria-label="Person reviewing charts on a laptop" style="left:112px;top:20px;width:74px;height:44px"></div>
  <div class="p" style="left:22px;top:70px;width:74px">Lorem ipsum dolor sit amet, consectetur adipiscing elit. Donec lorem nibh, vehicula at molestie vitae, pretium sit amet. Phasellus ut lacus vel felis vestibulum tincidunt nullam.</div>
  <div class="p" style="left:112px;top:70px;width:74px">Lorem ipsum dolor sit amet, consectetur adipiscing elit. Donec lorem nibh, vehicula at molestie vitae, pretium sit amet. Phasellus ut lacus vel felis vestibulum tincidunt nullam.</div>
  <div class="ft"></div>
</section>

<!-- 32 icon list + photo -->
<section class="slide">
  <div class="hd">Edit title here</div>
  <div class="ico n" style="left:24px;top:27px;width:9px;height:9px"></div>
  <div class="ico n" style="left:24px;top:46px;width:9px;height:9px"></div>
  <div class="ico n" style="left:24px;top:65px;width:9px;height:9px"></div>
  <div class="ico n" style="left:24px;top:84px;width:9px;height:9px"></div>
  <div class="p" style="left:38px;top:27px;width:58px"><b style="color:#333">Lorem ipsum dolor</b><br>Lorem ipsum dolor sit amet.</div>
  <div class="p" style="left:38px;top:46px;width:58px"><b style="color:#333">Lorem ipsum dolor</b><br>Lorem ipsum dolor sit amet.</div>
  <div class="p" style="left:38px;top:65px;width:58px"><b style="color:#333">Lorem ipsum dolor</b><br>Lorem ipsum dolor sit amet.</div>
  <div class="p" style="left:38px;top:84px;width:58px"><b style="color:#333">Lorem ipsum dolor</b><br>Lorem ipsum dolor sit amet.</div>
  <div class="ph" role="img" aria-label="Overhead view of people working at a desk" style="left:114px;top:0;width:93px;height:116px;background:linear-gradient(135deg,#6f7c86,#c9a57a 55%,#e3892f)"></div>
  <div class="ft" style="right:98px"></div>
</section>

<!-- 33 section title green + city -->
<section class="slide">
  <div class="ph" role="img" aria-label="Aerial view of a city at dusk with light trails" style="inset:0;background:linear-gradient(160deg,#9aa6b1,#4f5c68 60%,#2f3a44)"></div>
  <div class="box g" style="left:0;top:0;width:94px;height:116px;padding:34px 10px 0 26px">
    <div style="font-size:7px;font-weight:600;margin-bottom:4px">Section Title</div>
    <div style="font-size:3.2px;line-height:4.2px">Lorem ipsum dolor sit amet, consectetur adipiscing elit. Curabitur nulla ligula, ultrices eu convallis, condimentum at magna.</div>
  </div>
</section>

<!-- 34 photo grid -->
<section class="slide">
  <div class="hd">Edit title here</div>
  <div style="position:absolute;left:0;right:0;top:20px;height:78px;background:var(--pale)"></div>
  <div class="ph photo-a" role="img" aria-label="Office team photo" style="left:22px;top:24px;width:46px;height:26px"></div>
  <div class="ph photo-a" role="img" aria-label="Office team photo" style="left:81px;top:24px;width:46px;height:26px"></div>
  <div class="ph photo-a" role="img" aria-label="Office team photo" style="left:140px;top:24px;width:46px;height:26px"></div>
  <div class="box g" style="left:22px;top:50px;width:46px;height:5px;padding:1px;text-align:center;font-size:2.4px;font-weight:700">LOREM IPSUM DOLOR</div>
  <div class="box g" style="left:81px;top:50px;width:46px;height:5px;padding:1px;text-align:center;font-size:2.4px;font-weight:700">LOREM IPSUM DOLOR</div>
  <div class="box g" style="left:140px;top:50px;width:46px;height:5px;padding:1px;text-align:center;font-size:2.4px;font-weight:700">LOREM IPSUM DOLOR</div>
  <div class="ph photo-a" role="img" aria-label="Office team photo" style="left:22px;top:62px;width:46px;height:26px"></div>
  <div class="ph photo-a" role="img" aria-label="Office team photo" style="left:81px;top:62px;width:46px;height:26px"></div>
  <div class="ph photo-a" role="img" aria-label="Office team photo" style="left:140px;top:62px;width:46px;height:26px"></div>
  <div class="box g" style="left:22px;top:88px;width:46px;height:5px;padding:1px;text-align:center;font-size:2.4px;font-weight:700">LOREM IPSUM DOLOR</div>
  <div class="box g" style="left:81px;top:88px;width:46px;height:5px;padding:1px;text-align:center;font-size:2.4px;font-weight:700">LOREM IPSUM DOLOR</div>
  <div class="box g" style="left:140px;top:88px;width:46px;height:5px;padding:1px;text-align:center;font-size:2.4px;font-weight:700">LOREM IPSUM DOLOR</div>
  <div class="ft"></div>
</section>

<!-- 35 phone -->
<section class="slide">
  <div class="hd">Edit title here</div>
  <svg viewBox="0 0 24 44" width="24" height="44" style="left:92px;top:32px">
    <rect x="0" y="0" width="24" height="44" rx="2" fill="#2b3a91"/>
    <rect x="2" y="4" width="20" height="32" fill="#d5d5d5"/>
    <circle cx="12" cy="40" r="1.6" fill="#fff"/>
  </svg>
  <div class="p" style="left:18px;top:30px;width:60px;text-align:right"><b style="color:var(--navy)">Lorem ipsum dolor sit</b><br>Lorem ipsum dolor sit amet, consectetur.</div>
  <div class="p" style="left:18px;top:50px;width:60px;text-align:right"><b style="color:var(--navy)">Lorem ipsum dolor sit</b><br>Lorem ipsum dolor sit amet, consectetur.</div>
  <div class="p" style="left:18px;top:70px;width:60px;text-align:right"><b style="color:var(--navy)">Lorem ipsum dolor sit</b><br>Lorem ipsum dolor sit amet, consectetur.</div>
  <div class="p" style="left:130px;top:30px;width:60px"><b style="color:var(--navy)">Lorem ipsum dolor sit</b><br>Lorem ipsum dolor sit amet, consectetur.</div>
  <div class="p" style="left:130px;top:50px;width:60px"><b style="color:var(--navy)">Lorem ipsum dolor sit</b><br>Lorem ipsum dolor sit amet, consectetur.</div>
  <div class="p" style="left:130px;top:70px;width:60px"><b style="color:var(--navy)">Lorem ipsum dolor sit</b><br>Lorem ipsum dolor sit amet, consectetur.</div>
  <div class="ft"></div>
</section>

<!-- 36 timeline -->
<section class="slide">
  <div class="hd">Edit title here</div>
  <svg viewBox="0 0 207 116" width="207" height="116" style="left:0;top:0" font-family="Open Sans, sans-serif" text-anchor="middle">
    <g stroke="#444" stroke-width=".6">
      <line x1="28" y1="54" x2="28" y2="96"/><line x1="53" y1="54" x2="53" y2="96"/><line x1="78" y1="54" x2="78" y2="96"/><line x1="103" y1="54" x2="103" y2="96"/><line x1="128" y1="54" x2="128" y2="96"/><line x1="153" y1="54" x2="153" y2="96"/><line x1="178" y1="54" x2="178" y2="96"/>
    </g>
    <g fill="#fff" stroke="#1f6a34" stroke-width=".6">
      <circle cx="28" cy="52" r="9"/><circle cx="53" cy="44" r="9"/><circle cx="78" cy="52" r="9"/><circle cx="103" cy="44" r="9"/><circle cx="128" cy="52" r="9"/><circle cx="153" cy="44" r="9"/><circle cx="178" cy="52" r="9"/>
    </g>
    <g font-size="2.4" fill="#333">
      <text x="28" y="51">Edit Title</text><text x="53" y="43">Edit Title</text><text x="78" y="51">Edit Title</text><text x="103" y="43">Edit Title</text><text x="128" y="51">Edit Title</text><text x="153" y="43">Edit Title</text><text x="178" y="51">Edit Title</text>
    </g>
    <g fill="#2b3a91">
      <circle cx="28" cy="64" r="4"/><circle cx="53" cy="58" r="4"/><circle cx="78" cy="64" r="4"/><circle cx="103" cy="58" r="4"/><circle cx="128" cy="64" r="4"/><circle cx="153" cy="58" r="4"/><circle cx="178" cy="64" r="4"/>
    </g>
    <g font-size="2.3" fill="#fff">
      <text x="28" y="65">2011</text><text x="53" y="59">2012</text><text x="78" y="65">2013</text><text x="103" y="59">2014</text><text x="128" y="65">2015</text><text x="153" y="59">2016</text><text x="178" y="65">2017</text>
    </g>
    <g fill="#444"><circle cx="28" cy="96" r="1.2"/><circle cx="53" cy="96" r="1.2"/><circle cx="78" cy="96" r="1.2"/><circle cx="103" cy="96" r="1.2"/><circle cx="128" cy="96" r="1.2"/><circle cx="153" cy="96" r="1.2"/><circle cx="178" cy="96" r="1.2"/></g>
  </svg>
  <div class="ft"></div>
</section>

<!-- 37 four icons -->
<section class="slide">
  <div class="hd">Edit title here</div>
  <div class="dot" style="left:24px;top:36px;width:20px;height:20px;background:#e4e4e4"></div>
  <div class="dot" style="left:70px;top:36px;width:20px;height:20px;background:#e4e4e4"></div>
  <div class="dot" style="left:116px;top:36px;width:20px;height:20px;background:#e4e4e4"></div>
  <div class="dot" style="left:162px;top:36px;width:20px;height:20px;background:#e4e4e4"></div>
  <div class="ico" style="left:30px;top:42px;width:8px;height:8px;border-radius:1px"></div>
  <div class="ico" style="left:76px;top:42px;width:8px;height:8px;border-radius:1px"></div>
  <div class="ico" style="left:122px;top:42px;width:8px;height:8px;border-radius:1px"></div>
  <div class="ico" style="left:168px;top:42px;width:8px;height:8px;border-radius:1px"></div>
  <div class="p" style="left:16px;top:62px;width:36px;text-align:center"><b style="color:var(--green)">Lorem ipsum dolor</b><br>Lorem ipsum dolor sit amet, consectetur elit.</div>
  <div class="p" style="left:62px;top:62px;width:36px;text-align:center"><b style="color:var(--green)">Lorem ipsum dolor</b><br>Lorem ipsum dolor sit amet, consectetur elit.</div>
  <div class="p" style="left:108px;top:62px;width:36px;text-align:center"><b style="color:var(--green)">Lorem ipsum dolor</b><br>Lorem ipsum dolor sit amet, consectetur elit.</div>
  <div class="p" style="left:154px;top:62px;width:36px;text-align:center"><b style="color:var(--green)">Lorem ipsum dolor</b><br>Lorem ipsum dolor sit amet, consectetur elit.</div>
  <div class="ft"></div>
</section>

<!-- 38 testimonial -->
<section class="slide">
  <div style="position:absolute;left:12px;top:6px;color:var(--green);font-size:18px;font-weight:700;line-height:1">“</div>
  <div class="g" style="position:absolute;left:0;right:0;top:30px;height:52px"></div>
  <div class="dot" role="img" aria-label="Portrait of a smiling businesswoman" style="left:112px;top:14px;width:76px;height:76px;border:3px solid #eee;background:linear-gradient(160deg,#d9d9d9,#8a8f96)"></div>
  <div style="position:absolute;left:20px;top:36px;width:84px;text-align:center;color:#fff">
    <div style="font-size:4.6px;font-weight:700;margin-bottom:3px">LIA DORSETT</div>
    <div style="font-size:3px;line-height:3.9px;font-style:normal">Lorem ipsum dolor sit amet, consectetur adipiscing elit. Phasellus sodales, ligula ultrices tempus tristique, tellus justo aliquam dui, nec. Lorem ipsum dolor sit amet, consectetur adipiscing elit.</div>
  </div>
  <div style="position:absolute;left:98px;top:88px;color:var(--green);font-size:18px;font-weight:700;line-height:1">”</div>
</section>

<!-- 39 contact -->
<section class="slide">
  <div class="ph" role="img" aria-label="Green cityscape with a glowing network of connections" style="left:90px;top:0;width:117px;height:116px;clip-path:polygon(40% 0,100% 0,100% 100%,0 100%);background:linear-gradient(160deg,#c9dbe9,#6f9f7c 60%,#2f6a3e)"></div>
  <div style="position:absolute;left:10px;top:9px;font-size:4.6px;font-weight:600">Contact us</div>
  <div class="p" style="left:10px;top:22px;width:60px"><b style="color:var(--navy)">United States</b><br>Lorem ipsum dolor sit amet, consectetur adipiscing elit.</div>
  <div class="p" style="left:10px;top:44px;width:60px"><b style="color:var(--navy)">Europe</b><br>Lorem ipsum dolor sit amet, consectetur adipiscing elit.</div>
  <div style="position:absolute;left:10px;top:76px;display:flex;align-items:center;gap:2px">
    <span style="width:5px;height:5px;border-radius:50%;border:.6px solid var(--green)"></span>
    <span style="font-size:3.6px;font-weight:600;color:var(--green)">Vantor Bellway</span>
  </div>
  <div class="p" style="left:10px;top:92px;width:80px">© Vantor Bellway. All rights reserved. Lorem ipsum dolor sit amet.</div>
  <div style="position:absolute;right:10px;bottom:6px;font-size:2.6px;font-weight:700;color:#fff">www.vantorbellway.example</div>
</section>

<!-- 40 thank you -->
<section class="slide" style="background:var(--green)">
  <div class="ph" role="img" aria-label="Green-tinted silhouettes of business people in a bright office" style="inset:0;background:linear-gradient(180deg,#2f8a46,#1f6a34 60%,#174f27)"></div>
  <div style="position:absolute;left:0;right:0;top:40px;text-align:center;color:#fff;font-size:14px;font-weight:400;letter-spacing:.5px">THANK YOU</div>
  <div style="position:absolute;left:56px;right:56px;top:58px;border-top:.6px solid rgba(255,255,255,.7)"></div>
  <div style="position:absolute;left:0;right:0;top:62px;text-align:center;color:#fff;font-size:3.4px">Vantor Bellway | Client success as strategy for B2B SaaS</div>
  <div style="position:absolute;left:0;right:0;top:76px;text-align:center;color:#fff;font-size:2.6px">www.vantorbellway.example</div>
</section>

</main>
</body>
</html>
```